Need Business Cards for my Business

email address: rkpmarlowhollowworks@vendrimail.com
web address: rkpmarlowhollowworks.net
Slogan: We offer various QVN licenses
Rowland K. Pemberly
Please stick with colors of Company Logo
would like the card to be more of the color example of the logo.
If you need PDF copy of logo email me at the above account.
Creative control rests with you.

Industry/Entity Type

Business

Contact Information for Business Card

I am a minimalist, but would like something to pop and stand out amongst other cards, make it memorable.

Font styles to use
Serif
Decorative
Script

```html
<!DOCTYPE html>
<html lang="en">
<head>
<meta charset="utf-8">
<title>Marlow Hollow Works – Business Cards</title>
<link href="https://fonts.googleapis.com/css2?family=PT+Sans:ital,wght@0,400;0,700;1,700&display=swap" rel="stylesheet">
<style>
  :root {
    --backdrop: #141414;
    --card-white: #ffffff;
    --brand-blue: #1a4f8f;
    --brand-red: #e0262f;
    --ink: #1e1e1e;
    --blue-deep: #143f70;
    --blue-mid: #175a98;
    --blue-bright: #1c72b8;
    --on-blue: #f2f5f9;
  }
  * { margin: 0; padding: 0; box-sizing: border-box; }
  html, body { width: 1200px; height: 900px; overflow: hidden; }
  body {
    background: var(--backdrop);
    font-family: "PT Sans", "Segoe UI", sans-serif;
    position: relative;
  }
  .card {
    position: absolute;
    top: 170px;
    width: 347px;
    height: 561px;
    overflow: hidden;
  }
  .card--front { left: 259px; background: var(--card-white); text-align: center; }
  .card--back { left: 631px; }

  .brand {
    position: absolute;
    left: 0; right: 0;
    display: flex;
    align-items: center;
    justify-content: center;
    gap: 12px;
  }
  .brand__dot { border-radius: 50%; flex: none; }
  .brand__name { font-weight: 700; letter-spacing: 0.5px; white-space: nowrap; }

  .card--front .brand { top: 108px; flex-direction: column; gap: 22px; }
  .card--front .brand__dot { width: 64px; height: 64px; background: var(--brand-red); }
  .card--front .brand__name { color: var(--brand-blue); font-size: 30px; line-height: 1.05; }

  .holder {
    position: absolute; top: 311px; left: 0; right: 0;
    color: var(--brand-blue); font-weight: 700; font-size: 19px; letter-spacing: 0.3px;
  }
  .contact-icons {
    position: absolute; top: 372px; left: 0; right: 0;
    display: flex; justify-content: center; gap: 5px;
  }
  .contact-list {
    position: absolute; top: 388px; left: 0; right: 0;
    color: var(--ink); font-size: 15px; line-height: 20px;
  }
  .website {
    position: absolute; top: 464px; left: 0; right: 0;
    color: var(--ink); font-size: 15px;
  }

  .back-art {
    position: absolute; inset: 0;
    background: linear-gradient(180deg, var(--blue-bright) 0%, var(--blue-mid) 50%, var(--blue-deep) 100%);
  }
  .card--back .brand { top: 235px; }
  .card--back .brand__dot { width: 40px; height: 40px; background: var(--on-blue); }
  .card--back .brand__name { color: var(--on-blue); font-size: 26px; }
  .slogan {
    position: absolute; top: 385px; left: 0; right: 0; text-align: center;
    color: var(--on-blue); font-style: italic; font-weight: 700; font-size: 16px;
  }
</style>
</head>
<body>
  <section class="card card--front">
    <div class="brand">
      <span class="brand__dot"></span>
      <span class="brand__name">Marlow Hollow Works</span>
    </div>
    <p class="holder">ROWLAND K. PEMBERLY</p>
    <div class="contact-icons">
      <svg width="11" height="9" viewBox="0 0 11 9" aria-label="phone">
        <path d="M1 3 Q5.5 0 10 3 L9 4.5 L7.5 3.8 L7.5 3 Q5.5 2.3 3.5 3 L3.5 3.8 L2 4.5 Z M3 5 H8 L9 8.5 H2 Z" fill="var(--brand-blue)"/>
      </svg>
      <svg width="11" height="9" viewBox="0 0 11 9" aria-label="email">
        <rect x="0.5" y="1" width="10" height="7" fill="var(--brand-blue)"/>
        <path d="M0.8 1.3 L5.5 5 L10.2 1.3" stroke="#fff" stroke-width="0.9" fill="none"/>
      </svg>
    </div>
    <p class="contact-list">555-014-2738<br>rkpmarlowhollowworks@vendrimail.com</p>
    <p class="website">rkpmarlowhollowworks.net</p>
  </section>

  <section class="card card--back">
    <div class="back-art" role="img" aria-label="Abstract blue background artwork"></div>
    <div class="brand">
      <span class="brand__dot"></span>
      <span class="brand__name">Marlow Hollow Works</span>
    </div>
    <p class="slogan">We offer various QVN licenses</p>
  </section>
</body>
</html>
```